New Business Card Design Project

I farm pacific oysters, once they are harvested they sell to seafood markets and processors. The main selling point of the product I have is that the oysters are grown on a very isolated stretch of coastline of the far west coast of south australia that has the purest sea water quality. It is also a very Eco friendly and self sustainable industry. The sea state in this particular area is quite rugged and that helps to sculpture the shells into a uniform and displayable half shell.

Industry/Entity Type

Farm

Requirements
Must have
• name: Tobias Crennan
phone no: 0487315042
e-mail: crennan_tob@quillpost.example
address: P.O box 7
gull point 5794 south Australia
Should not have
• do not include title/job description

```html
<!DOCTYPE html>
<html lang="en">
<head>
<meta charset="utf-8">
<title>Saltreach Oysters – Business Card</title>
<link href="https://fonts.googleapis.com/css2?family=Arimo:wght@400;700&display=swap" rel="stylesheet">
<style>
  :root {
    --backdrop: #bdbdbd;
    --backdrop-edge: #9c9c9c;
    --ocean-light: #3f86b4;
    --ocean-mid: #23608f;
    --ocean-deep: #163d63;
    --mark-blue: #3d6f9c;
    --royal: #1f4fa8;
    --royal-deep: #173c8a;
    --violet: #4a3ea0;
    --paper: #ffffff;
    --ink-light: #ffffff;
    --ink-soft: #d6e6f5;
  }
  * { box-sizing: border-box; margin: 0; padding: 0; }
  html, body { width: 1200px; height: 871px; overflow: hidden; }
  body {
    background: radial-gradient(ellipse at 50% 40%, var(--backdrop) 0%, var(--backdrop-edge) 100%);
    font-family: "Arimo", Arial, sans-serif;
    position: relative;
  }
  .card {
    position: absolute;
    width: 540px;
    height: 310px;
    overflow: hidden;
    box-shadow: 0 10px 28px rgba(0,0,0,0.35);
  }
  /* Front */
  .card-front {
    left: 40px; top: 280px;
    background: linear-gradient(160deg, var(--ocean-light) 0%, var(--ocean-mid) 45%, var(--ocean-deep) 100%);
    color: var(--ink-light);
    text-align: center;
  }
  .brand {
    position: absolute; left: 0; right: 0; top: 62px;
    display: flex; flex-direction: column; align-items: center;
  }
  .brand-mark {
    width: 74px; height: 74px; border-radius: 50%;
    background: var(--mark-blue);
    margin-bottom: 14px;
  }
  .brand-name {
    font-size: 34px; font-weight: 700; letter-spacing: 1px; color: var(--ink-light);
    line-height: 1.05;
  }
  .front-url {
    position: absolute; left: 0; right: 0; bottom: 42px;
    font-size: 11px; color: var(--ink-soft); letter-spacing: 0.5px;
  }
  /* Back */
  .card-back {
    left: 620px; top: 280px;
    background: var(--paper);
  }
  .back-shape { position: absolute; inset: 0; }
  .back-brand {
    position: absolute; left: 30px; top: 62px; width: 190px;
    display: flex; flex-direction: column; align-items: center;
  }
  .back-brand .brand-mark { width: 150px; height: 150px; margin-bottom: 10px; }
  .back-brand .brand-name { font-size: 16px; color: var(--royal-deep); }
  .contact {
    position: absolute; left: 326px; top: 96px;
    color: var(--ink-light);
  }
  .person-name { font-size: 21px; font-weight: 400; margin-bottom: 22px; }
  .address { font-size: 13px; line-height: 1.35; margin-bottom: 18px; }
  .contact-list { list-style: none; font-size: 12px; line-height: 1.65; }
  .contact-list li { display: flex; align-items: center; gap: 8px; white-space: nowrap; }
  .contact-list svg { width: 11px; height: 11px; flex: none; }
</style>
</head>
<body>
  <section class="card card-front" aria-label="Card front">
    <div class="brand">
      <div class="brand-mark"></div>
      <div class="brand-name">Saltreach Oysters</div>
    </div>
    <div class="front-url">www.saltreachoysters.example</div>
  </section>

  <section class="card card-back" aria-label="Card back">
    <svg class="back-shape" viewBox="0 0 540 310" preserveAspectRatio="none" aria-hidden="true">
      <defs>
        <linearGradient id="panelBlue" x1="0" y1="0" x2="1" y2="1">
          <stop offset="0" stop-color="#2a63bf"/>
          <stop offset="1" stop-color="#183f8f"/>
        </linearGradient>
      </defs>
      <path d="M236 0 H540 V310 H180 Q370 170 236 0 Z" fill="url(#panelBlue)"/>
      <path d="M180 310 Q370 170 236 0 L250 0 Q392 175 205 310 Z" fill="#5a86d6" opacity="0.55"/>
      <path d="M180 310 Q300 250 330 200 Q300 270 240 310 Z" fill="var(--violet)" opacity="0.8"/>
    </svg>
    <div class="back-brand">
      <div class="brand-mark"></div>
      <div class="brand-name">Saltreach Oysters</div>
    </div>
    <div class="contact">
      <div class="person-name">Tobias Crennan</div>
      <div class="address">P.O box 7<br>gull point 5794<br>South Australia</div>
      <ul class="contact-list">
        <li><svg viewBox="0 0 12 12"><rect x="3" y="0.5" width="6" height="11" rx="1.2" fill="none" stroke="#fff" stroke-width="1.2"/><circle cx="6" cy="9.5" r="0.8" fill="#fff"/></svg>0487315042</li>
        <li><svg viewBox="0 0 12 12"><rect x="0.6" y="2" width="10.8" height="8" fill="none" stroke="#fff" stroke-width="1.2"/><path d="M0.6 2 L6 6.5 L11.4 2" fill="none" stroke="#fff" stroke-width="1.2"/></svg>crennan_tob@quillpost.example</li>
        <li><svg viewBox="0 0 12 12"><circle cx="6" cy="6" r="5.3" fill="none" stroke="#fff" stroke-width="1.1"/><ellipse cx="6" cy="6" rx="2.3" ry="5.3" fill="none" stroke="#fff" stroke-width="1"/><path d="M0.8 6 H11.2" stroke="#fff" stroke-width="1"/></svg>www.saltreachoysters.example</li>
      </ul>
    </div>
  </section>
</body>
</html>
```